My Professional Resume/CV Design

Hi Pixel Harbor experts, I need a professional resume/CV design for using my carrier hiring activities. I have a draft and this draft is 2 types.
1) Traditional IT Major Company Senior(Manager Level) to Director level application (File: Tanabe_Mirei_Res_EN2023AprA)
>Application example companies: Velmora, Drant, Quenta, Tidewicket, VossLattice, Brisk Vale, Hexaplume, Korvani, Zuvetra, Ferno, uMox, Wirlpeak etc
>This should not be fancy. Please make format with traditional/gentle/standard but also need to appear unique point such as icons, borderlines etc
2) Cutting-Edge (Web 3.0/metaverse/NFT/Crypto) Start-up or Young (Less 5 year's history) Company Director and C-Levels position application (Tanabe_Mirei_Res_EN2023Apr_typeC)
>Application Example Companies: Perilux Studios, Quorvex, Nexlorry.net, Dovecrest, FarDune, KelpVaultix, Ravello, Zipo/Tolk/Verm, Plunket, VESKARD, quillNRX etc
>This resume format should be something "edge" "advanced" "future" and "high-tech", so need to your high sense of design technics.
Both drafts is without a profile picture, but I need to put in my portfolio picture (Just attached one is my 2018's, you can trim and edit as well)
For the document format, please send me to WORD and PAGES both. and total MAX 2 page in all contents please (No more 3 pages)
Target Market(s)
Traditional Major Tech Company's VP/Directors or/and Latest Web 3.0 StartUp C-Levels (CEO/CTO/CSO/COO etc)
Industry/Entity Type
Technology
Font styles to use
Other font styles liked:
- Choose 3 a)Century Gothic b) Avenir c)Graphik d)Kohinoor e)Optima f)Platino
Look and feel
Each slider illustrates characteristics of the customer's brand and the style your logo design should communicate.

```html
<!DOCTYPE html>
<html lang="en">
<head>
<meta charset="utf-8">
<title>Mirei Tanabe – Resume</title>
<link rel="stylesheet" href="https://fonts.googleapis.com/css2?family=Montserrat:wght@500;600;700;800&family=Didact+Gothic&display=swap">
<style>
:root{
  --plum:#7d2986;
  --plum-deep:#651e70;
  --magenta:#9c3a9e;
  --lilac:#c793ca;
  --lilac-soft:#e7d3e8;
  --ink:#2f2f33;
  --paper:#ffffff;
  --mist:#f1eff3;
  --backdrop:#dcdbe0;
}
*{box-sizing:border-box;margin:0;padding:0}
html,body{width:1050px;height:1200px;overflow:hidden}
body{background:var(--backdrop);font-family:"Didact Gothic",sans-serif;color:var(--ink);position:relative}
.page{position:absolute;top:240px;width:510px;height:721px;background:var(--paper);overflow:hidden;box-shadow:0 4px 14px rgba(0,0,0,.18)}
.page-profile{left:10px}
.page-experience{left:530px}

/* profile page */
.sidebar{position:absolute;left:0;top:0;width:181px;height:100%;background:linear-gradient(180deg,#8f3596 0%,var(--plum) 40%,var(--plum-deep) 100%)}
.corner-shape{position:absolute;right:0;top:0}
.portrait{position:absolute;left:128px;top:18px;width:122px;height:122px;border-radius:50%;background:radial-gradient(circle at 50% 45%,#8a8f9c 0%,#3c3f48 55%,#1e1f24 100%);border:3px solid var(--paper)}
.name{position:absolute;left:271px;top:14px;font-family:"Montserrat",sans-serif;font-weight:800;font-size:30px;line-height:33px;color:var(--plum);letter-spacing:.5px}
.location{position:absolute;left:271px;top:86px;font-family:"Montserrat",sans-serif;font-weight:600;font-size:12.5px;color:var(--magenta);letter-spacing:.3px}
.contact-email{position:absolute;left:196px;top:138px;font-family:"Montserrat",sans-serif;font-size:7.6px;font-weight:500;color:var(--paper);display:flex;align-items:center;gap:4px;white-space:nowrap}
.contact-phone{position:absolute;left:358px;top:133px;font-family:"Montserrat",sans-serif;font-size:12.5px;font-weight:700;color:var(--ink);display:flex;align-items:center;gap:8px;white-space:nowrap}
.competencies{position:absolute;left:9px;top:185px;width:164px;height:405px;border:1px dashed rgba(255,255,255,.35);padding:12px 10px}
.competencies h2{font-family:"Montserrat",sans-serif;font-weight:500;font-size:10.5px;color:var(--paper);letter-spacing:.3px;margin-bottom:6px}
.competencies ul{list-style:none}
.competencies li{font-size:7.6px;color:var(--paper);line-height:20.5px;padding-left:10px;position:relative;white-space:nowrap}
.competencies li::before{content:"";position:absolute;left:0;top:9px;width:2.5px;height:2.5px;border-radius:50%;background:var(--paper)}
.education{position:absolute;left:18px;top:600px;width:154px;height:78px;background:var(--magenta);padding:10px 11px;color:var(--paper)}
.education h2{font-family:"Montserrat",sans-serif;font-weight:500;font-size:10.5px;margin-bottom:7px}
.education p{font-family:"Montserrat",sans-serif;font-weight:600;font-size:6.6px;line-height:9px;margin-bottom:6px}
.summary{position:absolute;left:203px;top:172px;width:292px}
.headline{font-family:"Montserrat",sans-serif;font-weight:700;font-size:9.3px;line-height:12px;color:var(--magenta);margin-bottom:6px}
.tagline{font-size:7.6px;line-height:9.5px;margin-bottom:6px}
.summary p.body{font-size:6.9px;line-height:8.6px;margin-bottom:6px}
.summary .core{font-size:6.6px;font-weight:700;font-family:"Montserrat",sans-serif}
.highlights{position:absolute;left:197px;top:413px;width:304px;height:308px;background:var(--mist);padding:8px 6px 0}
.highlights-inner{border:1px dashed #b9b3bd;height:100%;padding:8px 9px}
.highlights h2{font-family:"Montserrat",sans-serif;font-weight:700;font-size:9.5px;color:var(--magenta);margin-bottom:6px}
.highlights ul{list-style:none}
.highlights li{font-size:7px;line-height:8.9px;text-align:justify;text-indent:8px;margin-bottom:11px}
.page-strip{position:absolute;left:0;bottom:0;width:100%;height:6px;background:linear-gradient(90deg,var(--plum),var(--lilac))}

/* experience page */
.exp-header{position:absolute;left:0;top:0;width:100%;height:46px;background:var(--plum);color:var(--paper);text-align:center;padding-top:7px}
.exp-header h1{font-family:"Montserrat",sans-serif;font-weight:600;font-size:13px;letter-spacing:.4px}
.exp-header p{font-family:"Montserrat",sans-serif;font-weight:500;font-size:7px;margin-top:5px}
.exp-column{position:absolute;top:56px;width:232px;height:650px;overflow:hidden}
.exp-left{left:15px}
.exp-right{left:263px}
.role{font-family:"Montserrat",sans-serif;font-weight:600;font-size:6.5px;line-height:8.4px;color:var(--magenta);margin:0 0 4px}
.exp-column p{font-size:6.2px;line-height:7.9px;margin-bottom:5px}
.exp-column p.justify{text-align:justify}
.exp-column b{font-family:"Montserrat",sans-serif;font-weight:600}
.exp-column .note{font-style:italic}
.gap{height:5px}
</style>
</head>
<body>

<section class="page page-profile">
  <div class="sidebar"></div>
  <svg class="corner-shape" width="330" height="170" viewBox="0 0 330 170">
    <polygon points="240,0 330,0 330,70" fill="#7d2986"/>
    <polygon points="290,0 330,0 330,38" fill="#c793ca"/>
    <polygon points="0,128 330,128 330,158 0,158" fill="#ecebee"/>
    <polygon points="0,128 160,128 148,158 0,158" fill="#651e70"/>
    <polygon points="160,128 170,128 158,158 148,158" fill="#9c3a9e"/>
  </svg>
  <div class="portrait" role="img" aria-label="Portrait photograph of the candidate in a light suit"></div>
  <h1 class="name">MIREI<br>TANABE</h1>
  <div class="location">WANCHAI, HONG KONG</div>
  <div class="contact-email">
    <svg width="10" height="7" viewBox="0 0 10 7"><rect x="0.5" y="0.5" width="9" height="6" fill="none" stroke="#fff"/><polyline points="0.5,0.5 5,4 9.5,0.5" fill="none" stroke="#fff"/></svg>
    mtanabe512@postlane.net
  </div>
  <div class="contact-phone">
    <svg width="11" height="11" viewBox="0 0 24 24"><path fill="#9c3a9e" d="M6.6 10.8a15.1 15.1 0 0 0 6.6 6.6l2.2-2.2c.3-.3.7-.4 1-.2 1.1.4 2.3.6 3.6.6.6 0 1 .4 1 1V20c0 .6-.4 1-1 1A17 17 0 0 1 3 4c0-.6.4-1 1-1h3.5c.6 0 1 .4 1 1 0 1.3.2 2.5.6 3.6.1.3 0 .7-.2 1z"/></svg>
    +852 5170 3386
  </div>

  <div class="competencies">
    <h2>CORE COMPETENCIES</h2>
    <ul>
      <li>Global Operations Management</li>
      <li>Strategic Partnerships</li>
      <li>Process Improvement Champion</li>
      <li>Strategic Planning &amp; Execution</li>
      <li>Cryptocurrency | B2B &amp; B2C</li>
      <li>Research &amp; Development</li>
      <li>Key Account Management</li>
      <li>Business Restructuring</li>
      <li>Team Leadership / Management</li>
      <li>P &amp; L / Revenue Growth</li>
      <li>Budget Management</li>
      <li>Sales B2B + B2G</li>
      <li>Staff Training / Retention</li>
      <li>Business Administration</li>
      <li>Supply Chain &amp; Logistics</li>
      <li>Vendor / Financial Management</li>
      <li>Negotiations &amp; Agreements</li>
      <li>Records &amp; Documentation</li>
    </ul>
  </div>
  <div class="education">
    <h2>EDUCATION</h2>
    <p>Bachelor's Degree in Economics / Philosophy</p>
    <p>University of Kasumi, Japan</p>
  </div>

  <div class="summary">
    <div class="headline">Business Development | Cutting Edge Technology | Partner Channel Sales</div>
    <div class="tagline">Wide-range Propose Ability / Strategic Planning &amp; Execution / Be As A Professional Middleman Between Japan/apac/global</div>
    <p class="body">My value and career will only increase in a diverse and multinational work environment High-impact growth-oriented professional demonstrating a strong grasp of current marketing tools and strategies aligned with Cutting-edge technology with an interest in the transformation of society/era events within the industry and cyber security with an Entrepreneurial sprit. Strategically collaborate with external vendors and internal business partners; manages various commercial platforms, systems, domains, and channels to ensure scale marketing and lead development capabilities in line with business growth plans that deliver high-quality results. Participate in supply chain strategy development, developing implementation plans, and methods of dealing with business. Display strong analytical ability to evaluate end-to-end customer experience across multiple channels and customer touchpoints. Highly creative with experience in identifying target audiences and devising digital campaigns while valuing traditional methods that engage, inform, and motivate while staying abreast of industry trends.</p>
    <p class="body"><span class="core">"Cutting-Edge Technologies" "Business Development" and "Japan/APAC Channel Sales"</span> <b>are my main core.</b></p>
  </div>

  <div class="highlights">
    <div class="highlights-inner">
      <h2>HIGHLIGHTS OF QUALIFICATION</h2>
      <ul>
        <li>• As Bridge to the gap of Japanese business culture faced by many non-Japanese companies. The Japanese market is potentially huge and digital transformation is lagging behind, there is a lot of opportunities to take a market share. Most of their weakness is "Culture Difference" rather than "language". I am a native Japanese, fluent English Speaker, and as a business developer is familiar with business practices in Japan/other than Japan, I have confidence fulfill the role of mutual understanding</li>
        <li>• Expert in conducting marketing research and analyzing data strategically to identify brand / product value proposition, prospect customers, markets, and major competitors while utilizing PM software (visualization with 5W1H details)</li>
        <li>• Understands target audiences and competition dynamics with insights from the various premise sources while leading integrated digital and offline marketing campaigns from concept to execution, on time and within scope and budget.</li>
        <li>• Serve as supply chain interfaces for all major projects, with clear knowledge in project progress, logistics and distribution development consideration with each customer journey, and implementation and execution from upper to lower streams.</li>
        <li>• Conceptualize and develop brand/product marketing plans and campaigns for companies and individual business lines, including planning, liaison, coordination and execution.</li>
      </ul>
    </div>
  </div>
  <div class="page-strip"></div>
</section>

<section class="page page-experience">
  <header class="exp-header">
    <h1>PROFESSIONAL EXPERIENCE</h1>
    <p>(&amp; *REASON FOR LEAVING WRITE END OF EACH CARRIER PARAGRAPH)</p>
  </header>

  <div class="exp-column exp-left">
    <h3 class="role">INSIDE RENEWALS SALES | HALVERN NETWORKS. | HONG KONG &nbsp;| &nbsp;JUL 2022 - PRESENT</h3>
    <p>First visa-sponsored employee since the establishment of the APAC Hong Kong company (2017 and in total over 100+). Promotion to Territory Manager (Inside New Sales) is factored in. The agreement to start with renewal sales was to be able to build relationships with existing partners and to set the stage for the new position. Due to internal circumstances, there is no budgetary visibility for an Inside Sales Manager for the Japan Territory. Job hunting activity while still employed for reasons of wanting to advance own careers external, as prospects for promotion within the company are very low expectations by company reasons.</p>
    <p>• Distributor and Reseller (Partner) Management: Before I join, Halvern was the low position for any of the partner's sales, like quotation production due to only focused PO. I focusing what end users face on the problems and pain and shared with proper partners. A result, they never ask me for a quotation (they now can quote themself) and they proposed me to new sales plans and strategies. I just concentrated to do what my partner want and relationship development.</p>
    <p>• Co-work with Territory Regional Team remotely: Mainly Japan Sales, SEs, CS, Technical Support</p>
    <p>• Enhancing mutual synergies with other regional teams: Corporate team works with especially APAC another region team ( India/SEA/ANZ/China total 4 regions) and US and EMEA as well.</p>
    <div class="gap"></div>
    <h3 class="role">BUSINESS DEVELOPMENT MANAGER | ORVANE HK LIMITED | HONG KONG &nbsp;| &nbsp;APR 2021- APR 2022</h3>
    <p>Join from GM's direct invitation because he wants to survive the pandemic crisis, this is an IT reseller business provider in Hong Kong, China, SEA, and Japan market. Upon long-term mainly prospective business development and strategy, then proposed better to downsizing and restructuring inclusive me, I suggest leaving this company and GM accepted (Still best relationships).</p>
    <p>• <b>As a Management Strategy and Business Development</b><br>Proposed various restructuring options including M&amp;A, collaboration with the competitors, high demanded IT solutions, Web Marketing campaigns especially for sleeping existing customers reclamation (Company running 30 years)</p>
    <p>• <b>Daily Operation as a CRM/Sales/Key Accounting</b><br>"One Stop Solutions" expert and salesperson as a 100+ client's information systems department. Providing 6 core IT-related services to located at both Hong Kong and China mainland B2B/ B2G based customers with respect and according to their requirements, corporate culture, size, nature, and policies.</p>
    <p>• <b>Involvement with client VC advisory service.</b><br>Seeking potential cutting-edge technology or software-related start-ups. Or performing technical due diligence and making judgments on the product of companies presented by the client-side for operating the best portfolio.</p>
    <div class="gap"></div>
    <h3 class="role">ADVISOR OF BUSINESS DEVELOPMENT| TELUMA HIGH-TECH (HONG KONG) LIMITED | HONG KONG &nbsp;| &nbsp;MAY 2020 – MAR 2021</h3>
    <p>I joined the company after contacting the person responsible for developing a medical digital device to prevent the COVID-19 pandemic and presenting the business to the company to achieve commercial success.</p>
    <p class="justify">• <b>Business development of organic disinfectant water creation devices</b><br>A new generation of organic disinfectant devices was launched at a part of medical places in Japan. Producing disinfectant water only with tap water and replacing alcohol. In order to bring the organization from being a group of developers to commercial professionals, various operations were required. Since a basic framework generates, the necessary tasks are identified, responsibilities were allocated to a proper person in charge, a business plan was drawn up with a rough timeline and scenario. Due to a change in policy, which focuses on commercial success in Japan before the Asian and global markets, I am no longer heavy responsibility for the project and am now involved just as a non-accountable advisor.</p>
  </div>

  <div class="exp-column exp-right">
    <p>• <b>Business Development of new flying mobility start-up</b><br>Development of a business plan for the production and development of the new Flying Mobility, the brainchild of the company's president. I've left this and hand over to the proper person such as the financial department for fundraising.<br>*Low expectations that the fundraising would be executed quickly, and a headhunting request from the GM of Orvane HK Limited.</p>
    <div class="gap"></div>
    <h3 class="role">BUSINESS DEVELOPMENT MANAGER | SABLE CREST GLOBAL | HONG KONG &nbsp;| &nbsp;APR2019 –MAR 2020</h3>
    <p class="justify">cutting-edge science such as human-type robots; creating program/production budgets and completed all interactions with the research institute on behalf of the TV station and also planned the 12 episodes of the first episode</p>
    <p>• Spearhead Japan and China's incorporation in the investigation and introduction of cutting-edge technology to which enhanced operational productivity and efficiency for Qaranis partners.<br>• In the Qaranis Ministry of Digital Affairs, presented Humanoid robotics usage for TV presenter collaborated with Qaranis National TV directors.<br>*Having received notification that funding from the Qaranis government has been frozen for six months due to the pandemic</p>
    <div class="gap"></div>
    <h3 class="role">HEAD OF DIVISION | NODEWAY TECH LIMITED (BRIGHTMERE GROUP (HOLDINGS) LTD. | HONG KONG | MAY 2016 – MAR 2019</h3>
    <p class="justify">Started work as one of the key players of Fin-Tech industry, Management, and head of operations of a platform for digital assets. When I first joined the company, it was just me as a junior manager + the CEO means actual 1 staff number, by 2018, the FinTech division had grown to 15 people in the Hong Kong office, over 100 people in total including BPO partners in Japan, the Philippines, Netherlands, etc. In this two-year period, I have achieved a total of 4 promotions and achieved my working carrier breakthroughs.</p>
    <p>• Outperformed corporate expectations in leading and supervising digital asset white label exchange operations by improving systems that cannot be managed before I join and implementing process improvement initiatives and manuals.</p>
    <p>• Adept in managing multiple projects, achieving stable operational exchange, contributing to end-user increase from 1.5K to 5K.</p>
    <p>• Nominated Taiwan subsidiary head of a startup, between May to Oct 2017, Spearhead global business operations while overseeing the Taiwan subsidiary business expansion to Taiwanese partner b2b clients and handover to the local manager.</p>
    <p>• Pioneered customized Digital Asset Exchange platform, process improvement initiatives, facilitating prompt delivery to clients.</p>
    <p>• Delivering digital assets to clients using exceptional customer service management to generate business while facilitating customers' integration wallet and listing exchange for each industry's digital asset. Total fund-raising amount was over US$ 1B.</p>
    <p>• Displayed solid leadership abilities in team-building / mentoring activities and optimized project branding processes involving HR oversight and staffing as well as financial control for each project.</p>
    <p>*As I could not expect any further promotion, I transfer to further develop my career and gain multi-national business acumen.</p>
    <div class="gap"></div>
    <h3 class="role">PROJECT MANAGER | PT. SERAYU BALI | TOKYO &amp; DENPASAR| 2014 – 2015</h3>
    <p>• Possessed a stellar review in the strategic planning of corporate projects with B2B institutions at Bali of Indonesia Microfinance and Property Corporate.<br><span class="note">*Relocate to Hong Kong by my personal reason at the time late of 2015</span></p>
    <div class="gap"></div>
    <h3 class="role">CHIEF OPERATION OFFICER | MERIDIA AGENCY | TOKYO| &nbsp;2010 – 2014</h3>
    <p>• Structured and pioneered the process of running the Tokyo branch of a Singaporean restaurant by connecting with the F&amp;B company. Demonstrated strength in PR including the English Media to increase brand awareness and clientele growth.<br><span class="note">*The business cessation requirements of the JV Agreement are met. (Reason cannot be given due to confidentiality, but I can answer orally.)</span></p>
  </div>
  <div class="page-strip"></div>
</section>

</body>
</html>
```